High-End Executive Transportation

We need a business card to represent our high-end executive transportation company called KORVA Transportation. We would like designs for rectangular and square cards with rounded corners. We want the card to incorporate a QR code, www.korvatransportation.example on the back. The attached picture shows a picture of our vehicle and we would like the card to match the two-tone paint scheme with silver being on top and black being on the bottom. We want the card to be simple, but represent high-end.

The card needs to have a line for employee name, office and cell phone number, email address, and website.

```html
<!DOCTYPE html>
<html lang="en">
<head>
<meta charset="utf-8">
<title>KORVA Transportation — Square Business Card</title>
<link href="https://fonts.googleapis.com/css2?family=Jost:wght@300;400;600&display=swap" rel="stylesheet">
<style>
  :root {
    --canvas-bg: #dcdcdc;
    --card-black: #1f1f1f;
    --card-silver: #e9e9e7;
    --text-white: #ffffff;
    --text-faint: #3a3a3a;
  }
  html, body {
    margin: 0;
    padding: 0;
    width: 1200px;
    height: 900px;
    overflow: hidden;
    background: var(--canvas-bg);
  }
  .canvas {
    width: 1200px;
    height: 900px;
    display: flex;
    align-items: center;
    justify-content: center;
  }
  .card {
    position: relative;
    width: 600px;
    height: 600px;
    border-radius: 52px;
    overflow: hidden;
    background: var(--card-black);
    font-family: "Jost", sans-serif;
    color: var(--text-white);
  }
  .card__silver-band {
    position: absolute;
    left: 0;
    top: 0;
    width: 100%;
    height: 160px;
    background: var(--card-silver);
  }
  .card__content {
    position: absolute;
    left: 110px;
    top: 250px;
    right: 40px;
  }
  .employee-name {
    margin: 0 0 36px;
    font-size: 42px;
    font-weight: 300;
    letter-spacing: 0.5px;
    line-height: 1;
  }
  .employee-name__last {
    font-weight: 600;
  }
  .contact-list {
    list-style: none;
    margin: 0;
    padding: 0;
    font-size: 25px;
    font-weight: 300;
    line-height: 31px;
  }
  .company-name {
    position: absolute;
    left: 110px;
    bottom: 62px;
    margin: 0;
    font-size: 32px;
    font-weight: 300;
    color: var(--text-faint);
    letter-spacing: 0.5px;
  }
</style>
</head>
<body>
  <main class="canvas">
    <article class="card">
      <div class="card__silver-band"></div>
      <div class="card__content">
        <h1 class="employee-name">Name <span class="employee-name__last">Lastname</span></h1>
        <ul class="contact-list">
          <li class="contact-list__office">32 555 01 45</li>
          <li class="contact-list__cell">00 555 01 46</li>
          <li class="contact-list__email">email@korvatransportation.example</li>
          <li class="contact-list__web">www.korvatransportation.example</li>
        </ul>
      </div>
      <p class="company-name">KORVA Transportation</p>
    </article>
  </main>
</body>
</html>
```